Telvor Enterprises has 5 divisions in the organisation.
One of them is our Soaps, Candles and Cosmetics range.

Our Logo is a ORVALE with the word ORVALE an image of a crown.
Orvale Supplements & Orvale Sports are 2 divisions.

Now we need to introduce our ORVALE COLLECTIONS which will include cosmetic, candles, fragrances etc.

What we need designed is an elegant, sophisticated label of our CANDLE JARS and Outer Box.

The same will flow through to our soaps and other collection.

This will the beginning of a long term relationship for the designer to maintain and update our Orvale Collections artwork.

Hello designers,

We have increases our 1st prize budget to $200.00

Please read the brief carefully.
We need this job wrapped up quickly.

It is a fairly simple project with huge long term potential.

We look forward to receiving some designs.

Reason: Due to the Easter Break last week, many people were off work. Therefore we have extended our deadline to allow other participants to submit their designs.

Reason: We have not found a design we like yet.

Industry/Entity Type

Cosmetics

Requirements
Must have
• The ORVALE and the word ORVALE must remain the same.
The word collections must be added under the crown.
The word collections to be Elegant, maybe cursive, or hand written.

Wording for Jar Label:
100% Soy Wax
Quality Essential oils & Fragrances
Hand made in Australia

Box Wording:
will be provided at later stage.
Make a mockup of a box but not too loud.
Sophisticated and elegant.
Do not use existing artwork from others.

Nice to have
• Special design label.

The width of the label to be no more than 50mm.
The height of the label to be no more than 60mm

We believe that the JAR label needs to be small and effective.
We beleive the box should use Royal colours and not too many flowers and vines. Elegance.
Should not have
• Should not be noisy, loud and full of information.

```html
<!DOCTYPE html>
<html lang="en">
<head>
<meta charset="utf-8">
<title>Orvale Collection – Candle Jar Label</title>
<link href="https://fonts.googleapis.com/css2?family=Great+Vibes&family=Arimo:wght@400;700&display=swap" rel="stylesheet">
<style>
  :root {
    --canvas-bg: #ffffff;
    --canvas-edge: #3d2455;
    --royal-purple: #3f2656;
    --royal-purple-deep: #361f4b;
    --gold: #c8ad5c;
    --gold-light: #d9c47e;
    --gold-dark: #9f8640;
  }
  * { box-sizing: border-box; margin: 0; padding: 0; }
  html, body {
    width: 1200px;
    height: 777px;
    overflow: hidden;
    background: var(--canvas-bg);
  }
  .canvas {
    position: relative;
    width: 1200px;
    height: 777px;
    border: 2px solid var(--canvas-edge);
    background: var(--canvas-bg);
  }
  .label {
    position: absolute;
    left: 377px;
    top: 120px;
    width: 446px;
    height: 537px;
    padding: 14px;
    background: linear-gradient(135deg, var(--gold-dark), var(--gold-light) 45%, var(--gold) 70%, var(--gold-dark));
  }
  .label-field {
    position: relative;
    width: 100%;
    height: 100%;
    background: radial-gradient(ellipse at 50% 45%, var(--royal-purple) 0%, var(--royal-purple-deep) 100%);
    color: var(--gold);
    text-align: center;
  }
  .label-field > * {
    position: absolute;
    left: 0;
    right: 0;
  }
  .collection-title {
    top: 28px;
    font-family: "Great Vibes", cursive;
    font-size: 66px;
    line-height: 1;
    font-weight: 400;
  }
  .product-claims {
    top: 137px;
    font-family: "Arimo", Arial, sans-serif;
    font-size: 16px;
    line-height: 28px;
  }
  .brand-name {
    top: 248px;
    font-family: "Arimo", Arial, sans-serif;
    font-weight: 700;
    font-size: 19px;
    letter-spacing: 0.5px;
  }
  .crown-emblem {
    left: 145px;
    right: auto;
    top: 296px;
    width: 127px;
    height: 109px;
    background: radial-gradient(ellipse at 50% 60%, rgba(200,173,92,0.35), rgba(200,173,92,0.08) 70%);
    border-radius: 6px;
  }
  .origin-line {
    top: 430px;
    font-family: "Great Vibes", cursive;
    font-size: 26px;
    line-height: 1.2;
  }
  .flourish {
    left: 138px;
    right: auto;
    top: 466px;
    width: 143px;
    height: 42px;
    background: linear-gradient(90deg, rgba(200,173,92,0.05), rgba(200,173,92,0.3) 50%, rgba(200,173,92,0.05));
    border-radius: 20px;
  }
</style>
</head>
<body>
  <main class="canvas">
    <section class="label" aria-label="Orvale Collection candle jar label">
      <div class="label-field">
        <h1 class="collection-title">Collection</h1>
        <p class="product-claims">100% Soy Wax<br>Quality Essential Oils &amp; Fragrances</p>
        <p class="brand-name">ORVALE</p>
        <div class="crown-emblem" role="img" aria-label="Large gold line-drawn crown emblem"></div>
        <p class="origin-line">Hand made in Australia</p>
        <div class="flourish" role="img" aria-label="Pair of gold scroll flourishes"></div>
      </div>
    </section>
  </main>
</body>
</html>
```